UI/ UX Design for ERP Software

We need a new UX/UI interface for a ERP software for property managers. Our CMMS / ERP solution is made based on responsive design technologies and is coded in PHP.
The overall UX to be similar to Tarn Vexa - easy navigation, intuitive menus.

Industry/Entity Type

Property Management

Number of Pages Required

5+ page

Requirements
Must have
• Round dock buttons
Consistent icons across the application
Enough Spacing between buttons/icons/ menu
Consistent Font
Nice to have
• We would like the UX to allow the users to use the application without /minimum training.
Should not have
• we don't want anything that is classic with respect to UX

```html
<!DOCTYPE html>
<html lang="en">
<head>
<meta charset="utf-8">
<title>Lotiva – Dashboard</title>
<link href="https://fonts.googleapis.com/css2?family=IBM+Plex+Sans:wght@400;500;600;700&display=swap" rel="stylesheet">
<style>
:root{
  --page:#e4f6fd;
  --header-a:#0a84f5;
  --header-b:#05c3fd;
  --band:#05c7fd;
  --active:#0a7cf5;
  --accent:#18b3f3;
  --ink:#222;
  --muted:#666;
  --grid:#cfcfcf;
  --blue-area:#82ade6;
  --orange-area:#f5a45d;
  --white:#fff;
}
*{box-sizing:border-box;margin:0;padding:0}
html,body{width:1152px;height:1200px;overflow:hidden}
body{background:var(--page);font-family:"IBM Plex Sans",sans-serif;color:var(--ink);position:relative}
.topbar{position:absolute;left:0;top:0;width:1152px;height:82px;background:linear-gradient(180deg,var(--header-a),var(--header-b))}
.menu-btn{position:absolute;left:49px;top:34px;width:15px;height:13px}
.brand{position:absolute;left:92px;top:22px;display:flex;align-items:center;gap:9px;color:var(--white);font-size:31px;font-weight:600;letter-spacing:.3px}
.brand-mark{width:20px;height:20px;border-radius:50%;background:var(--white)}
.search{position:absolute;left:415px;top:17px;width:427px;height:44px;background:#f4f4f4;border-radius:3px;display:flex;align-items:center;padding:0 18px;color:#888;font-size:14px;justify-content:space-between}
.bell{position:absolute;left:897px;top:32px}
.avatar{position:absolute;left:955px;top:14px;width:52px;height:52px;border-radius:50%;background:linear-gradient(160deg,#c9b9aa,#5b4c44)}
.presence{position:absolute;left:997px;top:17px;width:12px;height:12px;border-radius:50%;background:#22e01e}
.user-name{position:absolute;left:1019px;top:29px;color:var(--white);font-size:16px;font-weight:500;letter-spacing:.3px}
.stat{position:absolute;top:115px;transform:translateX(-50%);text-align:center;white-space:nowrap}
.stat-label{font-size:14px;color:var(--muted);font-weight:500;letter-spacing:.2px}
.stat-value{margin-top:4px;font-size:20px;color:var(--accent);display:flex;align-items:center;justify-content:center;gap:6px}
.panel{position:absolute;left:34px;top:195px;width:1070px;height:629px;background:var(--white);box-shadow:0 1px 4px rgba(0,0,0,.15);border-radius:3px;overflow:hidden}
.range-tabs{height:69px;background:var(--band);position:relative}
.tab{position:absolute;top:12px;height:45px;display:flex;align-items:center;gap:5px;color:var(--white);font-size:14px;font-weight:600;white-space:nowrap;transform:translateX(-50%)}
.tab.active{background:var(--active);border-radius:3px;padding:0 9px}
.range-date{position:absolute;left:54px;top:99px;color:var(--active);font-size:14px;font-weight:500}
.chart{position:absolute;left:0;top:69px}
.legend{position:absolute;width:320px;height:60px;background:var(--white);box-shadow:0 1px 3px rgba(0,0,0,.25);border-radius:2px;display:flex;align-items:center;padding-left:11px;gap:7px;font-size:16px;font-weight:500;color:var(--ink)}
.swatch{width:23px;height:23px;flex:none}
.footer-rule{position:absolute;left:0;top:1125px;width:1152px;height:1px;background:#b5c3c9}
.footer-code{position:absolute;left:1088px;top:1160px;font-size:11px;color:var(--active)}
</style>
</head>
<body>
<header class="topbar">
  <svg class="menu-btn" viewBox="0 0 15 13"><rect y="0" width="15" height="2.4" fill="#fff"/><rect y="5.3" width="15" height="2.4" fill="#fff"/><rect y="10.6" width="15" height="2.4" fill="#fff"/></svg>
  <div class="brand"><span class="brand-mark"></span>Lotiva</div>
  <div class="search"><span>Search</span>
    <svg width="14" height="14" viewBox="0 0 14 14"><circle cx="6" cy="6" r="4.5" fill="none" stroke="#222" stroke-width="2"/><line x1="9.3" y1="9.3" x2="13" y2="13" stroke="#222" stroke-width="2.2"/></svg>
  </div>
  <svg class="bell" width="16" height="18" viewBox="0 0 16 18"><path d="M8 1c3 0 5 2.3 5 5.5v4l2 2.5H1l2-2.5v-4C3 3.3 5 1 8 1z" fill="#fff"/><circle cx="8" cy="15.5" r="2" fill="#fff"/></svg>
  <div class="avatar" role="img" aria-label="User profile photo"></div>
  <div class="presence"></div>
  <div class="user-name">RAVI HOLM</div>
</header>

<div class="stat" style="left:119px"><div class="stat-label">PROPERTIES</div><div class="stat-value"><svg width="18" height="16" viewBox="0 0 18 16"><path d="M9 1 1 8h2.5v7h4.5v-4.5h2V15h4.5V8H17z" fill="#18b3f3"/></svg>3</div></div>
<div class="stat" style="left:259px"><div class="stat-label">TENANTS</div><div class="stat-value"><svg width="23" height="18" viewBox="0 0 23 18"><circle cx="11.5" cy="5" r="3.6" fill="#18b3f3"/><circle cx="4.5" cy="6" r="2.6" fill="#18b3f3"/><circle cx="18.5" cy="6" r="2.6" fill="#18b3f3"/><path d="M5.5 18c0-5 2.5-8 6-8s6 3 6 8z" fill="#18b3f3"/><path d="M0 15c0-3 2-5 4.5-5 1 0 1.8.3 2.4.8C5.6 12 5 13.5 5 15z" fill="#18b3f3"/><path d="M23 15c0-3-2-5-4.5-5-1 0-1.8.3-2.4.8 1.3 1.2 1.9 2.7 1.9 4.2z" fill="#18b3f3"/></svg>8</div></div>
<div class="stat" style="left:448px"><div class="stat-label">TOTAL PROPERTIES AREA</div><div class="stat-value"><svg width="20" height="20" viewBox="0 0 20 20"><path d="M10 0l3 3.5h-2v5.5h5.5v-2l3.5 3-3.5 3v-2H11v5.5h2L10 20l-3-3.5h2V11H3.5v2L0 10l3.5-3v2H9V3.5H7z" fill="#18b3f3"/></svg>422,000.00 sq.ft.</div></div>
<div class="stat" style="left:681px"><div class="stat-label">RENTED AREA</div><div class="stat-value"><svg width="20" height="20" viewBox="0 0 20 20"><path d="M10 0l3 3.5h-2v5.5h5.5v-2l3.5 3-3.5 3v-2H11v5.5h2L10 20l-3-3.5h2V11H3.5v2L0 10l3.5-3v2H9V3.5H7z" fill="#18b3f3"/></svg>233,500.00 sq.ft.</div></div>
<div class="stat" style="left:912px"><div class="stat-label">VACANCIES AREA</div><div class="stat-value"><svg width="20" height="20" viewBox="0 0 20 20"><path d="M10 0l3 3.5h-2v5.5h5.5v-2l3.5 3-3.5 3v-2H11v5.5h2L10 20l-3-3.5h2V11H3.5v2L0 10l3.5-3v2H9V3.5H7z" fill="#18b3f3"/></svg>188,500.00 sq.ft.</div></div>

<section class="panel">
  <nav class="range-tabs">
    <div class="tab active" style="left:265px"><svg width="12" height="12" viewBox="0 0 12 12"><circle cx="6" cy="6" r="5" fill="none" stroke="#fff" stroke-width="1.8"/><path d="M6 3v3.3H3.8" fill="none" stroke="#fff" stroke-width="1.5"/></svg>Last 7 days</div>
    <div class="tab" style="left:392px"><svg width="12" height="12" viewBox="0 0 12 12"><circle cx="6" cy="6" r="5" fill="none" stroke="#fff" stroke-width="1.8"/><path d="M6 3v3.3H3.8" fill="none" stroke="#fff" stroke-width="1.5"/></svg>Last months</div>
    <div class="tab" style="left:534px"><svg width="12" height="12" viewBox="0 0 12 12"><circle cx="6" cy="6" r="5" fill="none" stroke="#fff" stroke-width="1.8"/><path d="M6 3v3.3H3.8" fill="none" stroke="#fff" stroke-width="1.5"/></svg>&nbsp;Last 3 months</div>
    <div class="tab" style="left:655px"><svg width="12" height="12" viewBox="0 0 12 12"><circle cx="6" cy="6" r="5" fill="none" stroke="#fff" stroke-width="1.8"/><path d="M6 3v3.3H3.8" fill="none" stroke="#fff" stroke-width="1.5"/></svg>Next 7 day</div>
    <div class="tab" style="left:796px"><svg width="12" height="12" viewBox="0 0 12 12"><circle cx="6" cy="6" r="5" fill="none" stroke="#fff" stroke-width="1.8"/><path d="M6 3v3.3H3.8" fill="none" stroke="#fff" stroke-width="1.5"/></svg>Next months</div>
    <div class="tab" style="left:938px"><svg width="12" height="12" viewBox="0 0 12 12"><circle cx="6" cy="6" r="5" fill="none" stroke="#fff" stroke-width="1.8"/><path d="M6 3v3.3H3.8" fill="none" stroke="#fff" stroke-width="1.5"/></svg>&nbsp;Next 3 months</div>
  </nav>
  <div class="range-date">12/27/2020 - 01/03/2021</div>
  <svg class="chart" width="1070" height="559" viewBox="41 321 1300 679" font-family="IBM Plex Sans, sans-serif">
    <g stroke="var(--grid)" stroke-width="1">
      <line x1="137" y1="415" x2="1277" y2="415"/><line x1="137" y1="499" x2="1277" y2="499"/>
      <line x1="137" y1="582" x2="1277" y2="582"/><line x1="137" y1="666" x2="1277" y2="666"/>
      <line x1="137" y1="749" x2="1277" y2="749"/><line x1="137" y1="833" x2="1277" y2="833"/>
      <line x1="137" y1="917" x2="1277" y2="917"/>
      <line x1="137" y1="415" x2="137" y2="917"/><line x1="1277" y1="415" x2="1277" y2="917"/>
    </g>
    <g fill="#666" font-size="12" text-anchor="end">
      <text x="130" y="420">1.5</text><text x="130" y="504">1.25</text><text x="130" y="587">1</text>
      <text x="130" y="671">0.75</text><text x="130" y="754">0.5</text><text x="130" y="838">0.25</text><text x="130" y="921">0</text>
    </g>
    <path fill="var(--blue-area)" d="M137,917 C190,880 250,824 310,824 C360,824 380,850 420,870 L560,880 C600,800 650,752 707,752 C760,752 790,800 820,870 L960,870 C1000,790 1040,746 1080,746 C1130,746 1170,800 1200,850 L1277,917 Z"/>
    <path fill="var(--orange-area)" d="M137,917 C250,900 330,870 395,812 C440,760 480,738 505,738 C540,738 570,770 610,820 C650,870 670,883 693,883 C740,883 790,780 820,718 C840,670 860,649 885,649 C915,649 940,680 958,710 C1000,790 1030,890 1100,890 C1130,890 1150,870 1170,850 L1277,753 L1277,917 Z"/>
    <g fill="#10c6f5"><circle cx="269" cy="835" r="3.5"/><circle cx="707" cy="752" r="3.5"/><circle cx="1050" cy="752" r="3.5"/></g>
    <g fill="#0a7cf5"><circle cx="505" cy="738" r="3.5"/><circle cx="885" cy="649" r="3.5"/><circle cx="1275" cy="753" r="3.5"/></g>
    <g fill="#666" font-size="12" text-anchor="middle">
      <text x="206" y="949">27 Dec 2020</text><text x="350" y="949">28 Dec 2020</text><text x="494" y="949">29 Dec 2020</text>
      <text x="638" y="949">30 Dec 2020</text><text x="783" y="949">31 Dec 2020</text><text x="926" y="949">01 Jan 2021</text>
      <text x="1070" y="949">02 Jan 2021</text><text x="1214" y="949">03 Jan 2021</text>
    </g>
  </svg>
</section>

<div class="legend" style="left:37px;top:849px"><span class="swatch" style="background:#7fb1ea"></span>Scheduled Maintenance</div>
<div class="legend" style="left:378px;top:849px"><span class="swatch" style="background:#8def7c"></span>Completed Scheduled Maintenance</div>
<div class="legend" style="left:718px;top:849px"><span class="swatch" style="background:#f2a25c"></span>Future Scheduled Maintenance</div>
<div class="legend" style="left:37px;top:931px"><span class="swatch" style="background:#434348"></span>Scheduled Work Orders</div>
<div class="legend" style="left:378px;top:931px"><span class="swatch" style="background:#8585ea"></span>Completed Work Orders</div>
<div class="legend" style="left:718px;top:931px"><span class="swatch" style="background:#e95f84"></span>Property Inspections in Progress</div>
<div class="legend" style="left:37px;top:1014px"><span class="swatch" style="background:#e3d85c"></span>Completed Property Inspections</div>

<div class="footer-rule"></div>
<div class="footer-code">C 43</div>
</body>
</html>
```